Velsori Biotechnology needs a professional powerpoint design

We would like to re-design our powerpoint template(as attachment 1), it should be based on our current logo (as attachment 2). We hope the new powerpoint template could be more professional and like a biotechnology company with advanced technology.
Velsori Biotechnology is a contract development and manufacturing organization to provide high quality services to our clients in development, lead-in advanced technology and cGMP manufacturing of biopharmaceuticals from clinical to commercial manufacturing. We offers the advanced technology and services to become the best partner for clients from clinical to commercial manufacturing.
Reason: We would like to extend the deadline for this project so that designers can have more time to prepare, thanks.
Target Market(s)
Velsori Biotechnology is a contract development and manufacturing organization to provide high quality services to our clients in development, lead-in advanced technology and cGMP manufacturing of biopharmaceuticals from clinical to commercial manufacturing.
Velsori primary focus on development and manufacturing of glycoprotein pharmaceuticals against breast cancer, supplies KEP Taiwan with KEP-437 & KEP-438 for global clinical trials and commercialization in the future. Velsori offers the advanced technology and services to become the best partner for clients from clinical to commercial manufacturing.
Industry/Entity Type
Biotechnology
Requirements
Must have
- The new powerpoint design should based on our current logo.
Should not have
- The similar design with current powerpoint style. Please don't refer the design style of our current website http://www.velsori-example.com.tw/ as well, we will re-design it soon.

```html
<!DOCTYPE html>
<html lang="en">
<head>
<meta charset="utf-8">
<title>Velsori Biotechnology – Slide Overview</title>
<link href="https://fonts.googleapis.com/css2?family=PT+Sans+Narrow:wght@700&family=Roboto+Slab:wght@400;700&family=Roboto:wght@400;700&display=swap" rel="stylesheet">
<style>
:root{
  --page:#141414;
  --sheet:#c6c9ce;
  --slide:#ffffff;
  --ink:#333333;
  --muted:#8a8a8a;
  --amber:#ffa500;
  --orange:#ff7a00;
  --red:#ff3c00;
  --amber-dark:#e59400;
  --orange-dark:#e96a00;
  --red-dark:#c92a00;
  --slate:#3d3d3d;
  --grey:#8a8a8a;
  --panel:#e6e6e6;
  --heading:#3a3a3a;
}
*{margin:0;padding:0;box-sizing:border-box}
html,body{width:1200px;height:800px;overflow:hidden;background:var(--page)}
body{position:relative;font-family:"Roboto",sans-serif;color:var(--ink)}
.sheet-title{position:absolute;top:22px;left:0;width:1200px;text-align:center;font-family:"PT Sans Narrow",sans-serif;font-size:36px;color:var(--heading);letter-spacing:.5px}
.sheet{position:absolute;left:18px;top:107px;width:1174px;height:611px;background:var(--sheet)}
.slide{position:absolute;width:371px;height:278px;background:var(--slide);overflow:hidden}
.selection{position:absolute;left:806px;top:415px;width:381px;height:288px;border:2px solid #fff}
.slide-no{position:absolute;font:700 10px "Roboto",sans-serif;color:var(--ink)}
.slide-mark{position:absolute;width:9px;height:9px}
.subtitle{position:absolute;top:12px;width:100%;text-align:center;font-size:5px;color:var(--orange)}
.title{position:absolute;top:25px;width:100%;text-align:center;font-family:"Roboto Slab",serif;font-size:16px;color:var(--ink)}
.rule{position:absolute;top:48px;left:176px;width:19px;height:1px;background:var(--orange)}
.brand{position:absolute;left:27px;top:252px;font:700 10px "Roboto",sans-serif;color:var(--slate);letter-spacing:.5px;display:flex;align-items:center;gap:3px}
.brand i{display:block;width:7px;height:7px;border-radius:50%;background:var(--amber)}
.tiny{font-size:4.4px;line-height:6px;color:var(--orange)}
.item-title{font-size:6px;font-weight:700;color:var(--ink);line-height:8px}
/* slide 1 */
.sq{position:absolute;width:26px;height:26px}
.sq.a{background:var(--amber)}.sq.b{background:var(--orange)}
.sq-text{position:absolute;width:100px}
/* slide 2 */
.article{position:absolute;left:18px;top:114px;width:130px}
.article h3{font:400 8px "Roboto Slab",serif;color:var(--ink);margin-bottom:4px}
.article h3 span{color:var(--orange)}
.article p{font-size:4.6px;line-height:7.2px;color:var(--orange);text-align:justify}
.svc{position:absolute;width:80px}
.svc-icon{position:absolute;width:12px;height:14px}
/* slide 3 */
.photo{position:absolute;inset:0;background:linear-gradient(135deg,#dfe8f3 0%,#b9c8dc 35%,#5d7598 60%,#cfd9e6 85%,#eef2f7 100%)}
.photo-band{position:absolute;left:0;top:233px;width:326px;height:39px;background:rgba(255,255,255,.55)}
.photo-title{position:absolute;right:58px;top:241px;font:700 18px "Roboto Slab",serif;color:var(--amber)}
.photo-badge{position:absolute;left:333px;top:233px;width:38px;height:39px;background:#d9dde3;display:flex;align-items:center;justify-content:center}
/* slide 4 */
.org-box{position:absolute;background:var(--amber);color:#fff;font:700 6.5px "Roboto Slab",serif;text-align:center;line-height:13px}
.org-line{position:absolute;background:#9a9a9a}
.dept{position:absolute;top:138px;width:76px;height:76px;background:var(--panel)}
.dept h4{height:12px;background:var(--slate);color:#fff;font:700 5.5px "Roboto Slab",serif;text-align:center;line-height:12px}
.dept svg{display:block;margin:9px auto 0}
.dept ul{margin:6px 0 0 12px;font-size:3.8px;line-height:5.4px;color:var(--ink)}
/* slide 5 */
.donut{position:absolute;left:125px;top:90px}
.dlabel{position:absolute;width:56px}
.dlabel b{display:block;text-align:right;font:700 5px "Roboto Slab",serif;color:var(--ink)}
.dlabel p{font-size:3.6px;line-height:4.6px;color:var(--muted)}
/* slide 6 */
.steps{position:absolute;left:14px;top:118px}
.step-body{position:absolute;top:146px;height:48px;padding:6px 6px 0;font-size:4.6px;line-height:10px;color:#fff}
.step-body li{list-style:none}
.step-body li::before{content:"• "}
</style>
</head>
<body>
<h1 class="sheet-title">DESIGN Idea - 1g</h1>
<div class="sheet"></div>

<!-- Slide 37 -->
<section class="slide" style="left:23px;top:114px">
  <div class="subtitle">Insert subtitle here</div>
  <h2 class="title">Service Icons List</h2>
  <div class="rule"></div>
  <div class="sq a" style="left:31px;top:101px"></div>
  <div class="sq-text" style="left:65px;top:101px"><div class="item-title">Title-01</div><div class="tiny">Brief note on this service line.</div></div>
  <div class="sq b" style="left:31px;top:141px"></div>
  <div class="sq-text" style="left:65px;top:141px"><div class="item-title">Title-01</div><div class="tiny">Brief note on this service line.</div></div>
  <div class="sq a" style="left:31px;top:180px"></div>
  <div class="sq-text" style="left:65px;top:180px"><div class="item-title">Title-01</div><div class="tiny">Brief note on this service line.</div></div>
  <div class="sq b" style="left:195px;top:101px"></div>
  <div class="sq-text" style="left:228px;top:101px"><div class="item-title">Title-01</div><div class="tiny">Brief note on this service line.</div></div>
  <div class="sq a" style="left:195px;top:141px"></div>
  <div class="sq-text" style="left:228px;top:141px"><div class="item-title">Title-01</div><div class="tiny">Brief note on this service line.</div></div>
  <div class="sq b" style="left:195px;top:180px"></div>
  <div class="sq-text" style="left:228px;top:180px"><div class="item-title">Title-01</div><div class="tiny">Brief note on this service line.</div></div>
  <div class="brand"><i></i>VELSORI</div>
</section>

<!-- Slide 38 -->
<section class="slide" style="left:417px;top:114px">
  <div class="subtitle">Insert subtitle here</div>
  <h2 class="title">Service Icons List</h2>
  <div class="rule"></div>
  <div class="article">
    <h3>Article <span>Title</span></h3>
    <p>Velsori develops and manufactures biologics from early clinical work to commercial supply. Our teams combine process design, analytics and cGMP production under one roof, so partners move faster with fewer handoffs. Each project is planned with clear milestones, shared data and steady quality review.</p>
  </div>
  <svg class="svc-icon" style="left:173px;top:128px" viewBox="0 0 12 14"><rect x="3" y="0" width="6" height="3" fill="var(--orange)"/><rect x="1.5" y="3" width="9" height="11" rx="2" fill="none" stroke="var(--orange)" stroke-width="1.4"/><rect x="3.5" y="7" width="5" height="5" fill="var(--amber)"/></svg>
  <div class="svc" style="left:188px;top:127px"><div class="item-title">Title-01</div><div class="tiny">Short note about this service.</div></div>
  <svg class="svc-icon" style="left:270px;top:128px" viewBox="0 0 14 14"><circle cx="7" cy="7" r="1.6" fill="var(--red)"/><path d="M7 5 L4.5 0.8 A7 7 0 0 1 9.5 0.8Z M8.7 8 L13.5 8 A7 7 0 0 1 11 12.4Z M5.3 8 L3 12.4 A7 7 0 0 1 0.5 8Z" fill="var(--orange)"/></svg>
  <div class="svc" style="left:286px;top:127px"><div class="item-title">Title-02</div><div class="tiny">Short note about this service.</div></div>
  <svg class="svc-icon" style="left:173px;top:172px" viewBox="0 0 12 14"><circle cx="6" cy="2" r="2" fill="var(--orange)"/><rect x="2" y="4.5" width="8" height="5" rx="1.5" fill="var(--amber)"/><rect x="3.5" y="9.5" width="1.8" height="4.5" fill="var(--orange)"/><rect x="6.7" y="9.5" width="1.8" height="4.5" fill="var(--orange)"/></svg>
  <div class="svc" style="left:188px;top:172px"><div class="item-title">Title-03</div><div class="tiny">Short note about this service.</div></div>
  <svg class="svc-icon" style="left:270px;top:172px" viewBox="0 0 12 14"><path d="M6 0 C9 4 11 6 11 9 A5 5 0 0 1 1 9 C1 6 4 5 6 0Z" fill="var(--amber)"/><path d="M6 6 C7.5 8 8.5 9 8.5 10.5 A2.5 2.5 0 0 1 3.5 10.5 C3.5 9 5 8.5 6 6Z" fill="#fff"/></svg>
  <div class="svc" style="left:286px;top:172px"><div class="item-title">Title-04</div><div class="tiny">Short note about this service.</div></div>
  <div class="brand"><i></i>VELSORI</div>
</section>

<!-- Slide 39 -->
<section class="slide" style="left:810px;top:114px">
  <div class="photo" role="img" aria-label="Photo of a gloved scientist adjusting a sample slide on a laboratory microscope"></div>
  <div class="photo-band"></div>
  <div class="photo-title">Our Data &amp; Process</div>
  <div class="photo-badge">
    <svg width="22" height="22" viewBox="0 0 22 22" fill="none" stroke="var(--amber)" stroke-width="1.3"><path d="M2 20 V9 L8 5 V20"/><path d="M8 20 V2 H16 V20"/><path d="M11 6 h2 M11 9 h2 M11 12 h2"/><path d="M1 20 H21"/><circle cx="17" cy="15" r="3.5"/></svg>
  </div>
</section>

<!-- Slide 40 -->
<section class="slide" style="left:23px;top:421px">
  <div class="subtitle">Insert subtitle here</div>
  <h2 class="title">Organizational Structure</h2>
  <div class="rule"></div>
  <div class="org-box" style="left:158px;top:83px;width:56px">Board</div>
  <div class="org-line" style="left:185px;top:96px;width:1px;height:8px"></div>
  <div class="org-box" style="left:150px;top:104px;width:72px">Administration</div>
  <div class="org-line" style="left:185px;top:117px;width:1px;height:14px"></div>
  <div class="org-line" style="left:60px;top:131px;width:252px;height:1px"></div>
  <div class="org-line" style="left:60px;top:131px;width:1px;height:7px"></div>
  <div class="org-line" style="left:144px;top:131px;width:1px;height:7px"></div>
  <div class="org-line" style="left:228px;top:131px;width:1px;height:7px"></div>
  <div class="org-line" style="left:312px;top:131px;width:1px;height:7px"></div>
  <div class="dept" style="left:22px"><h4>Service Title-01</h4>
    <svg width="14" height="14" viewBox="0 0 14 14" fill="none" stroke="#555" stroke-width="1"><rect x="2" y="2" width="9" height="11"/><rect x="4.5" y="0.8" width="4" height="2.4" fill="#fff"/><path d="M4 6h5M4 8h5M4 10h5"/></svg>
    <ul><li>Service-01</li><li>Service-02</li><li>Service-03</li><li>Service-04</li></ul></div>
  <div class="dept" style="left:106px"><h4>Service Title-02</h4>
    <svg width="14" height="14" viewBox="0 0 14 14" fill="none" stroke="#555" stroke-width="1"><path d="M2 1 V5 A3 3 0 0 0 8 5 V1"/><path d="M5 8 V10 A2.5 2.5 0 0 0 10 10 V8"/><circle cx="10" cy="6.5" r="1.5"/></svg>
    <ul><li>Service-01</li><li>Service-02</li><li>Service-03</li><li>Service-04</li></ul></div>
  <div class="dept" style="left:190px"><h4>Service Title-03</h4>
    <svg width="14" height="14" viewBox="0 0 14 14" fill="none" stroke="#555" stroke-width="1"><path d="M7 12 L1.8 6.8 A3 3 0 0 1 7 3 A3 3 0 0 1 12.2 6.8Z"/><path d="M4 7 h2 l1-2 l1 4 l1-2 h1.5"/></svg>
    <ul><li>Service-01</li><li>Service-02</li><li>Service-03</li><li>Service-04</li></ul></div>
  <div class="dept" style="left:274px"><h4>Service Title-04</h4>
    <svg width="14" height="14" viewBox="0 0 14 14" fill="none" stroke="#555" stroke-width="1"><circle cx="7" cy="7" r="5.5"/><path d="M4 7 h6 M7 4 v6"/></svg>
    <ul><li>Service-01</li><li>Service-02</li><li>Service-03</li><li>Service-04</li></ul></div>
  <div class="brand"><i></i>VELSORI</div>
</section>

<!-- Slide 41 -->
<section class="slide" style="left:417px;top:421px">
  <div class="subtitle">Insert subtitle here</div>
  <h2 class="title">Data Circle</h2>
  <div class="rule"></div>
  <svg class="donut" width="120" height="120" viewBox="-60 -60 120 120">
    <g fill="none" stroke-width="22">
      <circle r="39" stroke="var(--amber)" stroke-dasharray="30.6 214.4" transform="rotate(-112.5)"/>
      <circle r="39" stroke="var(--orange)" stroke-dasharray="30.6 214.4" transform="rotate(-67.5)"/>
      <circle r="39" stroke="var(--amber)" stroke-dasharray="30.6 214.4" transform="rotate(-22.5)"/>
      <circle r="39" stroke="var(--orange)" stroke-dasharray="30.6 214.4" transform="rotate(22.5)"/>
      <circle r="39" stroke="var(--amber)" stroke-dasharray="30.6 214.4" transform="rotate(67.5)"/>
      <circle r="39" stroke="var(--orange)" stroke-dasharray="30.6 214.4" transform="rotate(112.5)"/>
      <circle r="39" stroke="var(--amber)" stroke-dasharray="30.6 214.4" transform="rotate(157.5)"/>
      <circle r="39" stroke="var(--orange)" stroke-dasharray="30.6 214.4" transform="rotate(202.5)"/>
    </g>
    <circle r="28" fill="#fff"/>
    <text y="-14" text-anchor="middle" font-size="5" fill="#999" font-family="Roboto,sans-serif">Title</text>
    <text y="4" text-anchor="middle" font-size="14" font-weight="700" fill="var(--ink)" font-family="Roboto,sans-serif">60%</text>
    <text y="13" text-anchor="middle" font-size="4.5" fill="#999" font-family="Roboto,sans-serif">Enter text</text>
    <g fill="#fff" stroke="var(--orange)" stroke-width="1.2">
      <circle cx="-18" cy="-42" r="9"/><circle cx="20" cy="-45" r="9"/><circle cx="46" cy="-17" r="9"/><circle cx="46" cy="23" r="9"/>
      <circle cx="20" cy="47" r="9"/><circle cx="-18" cy="48" r="9"/><circle cx="-47" cy="23" r="9"/><circle cx="-47" cy="-17" r="9"/>
    </g>
    <g fill="var(--orange)">
      <circle cx="-18" cy="-42" r="3.5"/><rect x="17" y="-48" width="6" height="6"/><path d="M42 -17 h8 l-4 4z"/><circle cx="46" cy="23" r="3.5"/>
      <path d="M17 47 h6 l-3 -4z"/><circle cx="-18" cy="48" r="3.5"/><rect x="-50" y="21" width="6" height="4"/><path d="M-51 -15 l4 -5 l4 5z"/>
    </g>
  </svg>
  <div class="dlabel" style="left:94px;top:91px"><b>Title</b><p>Short note on this data point.</p></div>
  <div class="dlabel" style="left:61px;top:129px"><b>Title</b><p>Short note on this data point.</p></div>
  <div class="dlabel" style="left:61px;top:167px"><b>Title</b><p>Short note on this data point.</p></div>
  <div class="dlabel" style="left:94px;top:199px"><b>Title</b><p>Short note on this data point.</p></div>
  <div class="dlabel" style="left:222px;top:95px"><b>Title</b><p>Short note on this data point.</p></div>
  <div class="dlabel" style="left:252px;top:127px"><b>Title</b><p>Short note on this data point.</p></div>
  <div class="dlabel" style="left:252px;top:166px"><b>Title</b><p>Short note on this data point.</p></div>
  <div class="dlabel" style="left:222px;top:199px"><b>Title</b><p>Short note on this data point.</p></div>
  <div class="brand"><i></i>VELSORI</div>
</section>

<!-- Slide 42 -->
<section class="slide" style="left:810px;top:421px">
  <div class="subtitle">Insert subtitle here</div>
  <h2 class="title">Stepwise Process</h2>
  <div class="rule"></div>
  <svg class="steps" width="350" height="36" viewBox="0 0 350 36">
    <path d="M0 10 H84 V0 L95 18 L84 36 V28 H0Z" fill="var(--amber-dark)"/>
    <path d="M84 10 H168 V0 L179 18 L168 36 V28 H84Z" fill="var(--orange-dark)"/>
    <path d="M168 10 H253 V0 L264 18 L253 36 V28 H168Z" fill="var(--red-dark)"/>
    <path d="M253 10 H337 V0 L348 18 L337 36 V28 H253Z" fill="var(--slate)"/>
    <g fill="none" stroke="#fff" stroke-width="1">
      <rect x="10" y="13" width="9" height="9" rx="1"/>
      <path d="M96 22 v-7 l3-2 l3 2 v7 M99 13 v9"/>
      <rect x="183" y="13" width="10" height="9"/><path d="M185 16 h6 M185 19 h6"/>
      <path d="M268 22 l8-8 l3 3 l-8 8z"/>
    </g>
    <g fill="#fff" font-family="Roboto,sans-serif" font-size="7" font-weight="700">
      <text x="32" y="21">Title-01</text><text x="116" y="21">Title-02</text><text x="200" y="21">Title-03</text><text x="284" y="21">Title-04</text>
    </g>
  </svg>
  <ul class="step-body" style="left:14px;width:84px;background:var(--amber)"><li>This is content in a line</li><li>This is content in a line</li></ul>
  <ul class="step-body" style="left:98px;width:84px;background:var(--orange)"><li>This is content in a line</li><li>This is content in a line</li></ul>
  <ul class="step-body" style="left:182px;width:85px;background:var(--red)"><li>This is content in a line</li><li>This is content in a line</li></ul>
  <ul class="step-body" style="left:267px;width:84px;background:var(--grey)"><li>This is content in a line</li><li>This is content in a line</li></ul>
  <div class="brand"><i></i>VELSORI</div>
</section>
<div class="selection"></div>

<!-- slide numbers -->
<svg class="slide-mark" style="left:23px;top:401px" viewBox="0 0 10 10"><path d="M5 1 L6.2 4 H9 L6.8 5.8 L7.6 9 L5 7.2 L2.4 9 L3.2 5.8 L1 4 H3.8Z" fill="none" stroke="#555" stroke-width=".8"/></svg>
<span class="slide-no" style="left:378px;top:398px">37</span>
<svg class="slide-mark" style="left:417px;top:401px" viewBox="0 0 10 10"><path d="M5 1 L6.2 4 H9 L6.8 5.8 L7.6 9 L5 7.2 L2.4 9 L3.2 5.8 L1 4 H3.8Z" fill="none" stroke="#555" stroke-width=".8"/></svg>
<span class="slide-no" style="left:772px;top:398px">38</span>
<svg class="slide-mark" style="left:810px;top:401px" viewBox="0 0 10 10"><path d="M5 1 L6.2 4 H9 L6.8 5.8 L7.6 9 L5 7.2 L2.4 9 L3.2 5.8 L1 4 H3.8Z" fill="none" stroke="#555" stroke-width=".8"/></svg>
<span class="slide-no" style="left:1166px;top:398px">39</span>
<svg class="slide-mark" style="left:23px;top:707px" viewBox="0 0 10 10"><path d="M5 1 L6.2 4 H9 L6.8 5.8 L7.6 9 L5 7.2 L2.4 9 L3.2 5.8 L1 4 H3.8Z" fill="none" stroke="#555" stroke-width=".8"/></svg>
<span class="slide-no" style="left:378px;top:704px">40</span>
<svg class="slide-mark" style="left:417px;top:707px" viewBox="0 0 10 10"><path d="M5 1 L6.2 4 H9 L6.8 5.8 L7.6 9 L5 7.2 L2.4 9 L3.2 5.8 L1 4 H3.8Z" fill="none" stroke="#555" stroke-width=".8"/></svg>
<span class="slide-no" style="left:772px;top:704px">41</span>
<svg class="slide-mark" style="left:810px;top:707px" viewBox="0 0 10 10"><path d="M5 1 L6.2 4 H9 L6.8 5.8 L7.6 9 L5 7.2 L2.4 9 L3.2 5.8 L1 4 H3.8Z" fill="none" stroke="#555" stroke-width=".8"/></svg>
<span class="slide-no" style="left:1166px;top:704px">42</span>
</body>
</html>
```